Criação de Apres. Comercial (com dobra) para Tecnologia & Ciencias
" A Brumel Soluções é uma empresa especializada em soluções personalizadas de TI .Em resumo, ela “cuida” de tudo para que os seus funcionários não precisem se preocupar ou perder tempo com problemas técnicos de informática, como computador e/ou internet, falta de segurança dos arquivos, ausência de backups, softwares desatualizados e muito mais. Com uma equipe proativa e altamente especializada, a Brumel Soluções consegue não apenas instalar os programas e equipamentos necessários como também realizar um monitoramento ativo para que a performance de todos os computadores da empresa se mantenha a mais elevada possível - 24 horas por dia, sete dias por semana. "

```html
<!DOCTYPE html>
<html lang="pt-BR">
<head>
<meta charset="utf-8">
<title>Brumel Soluções – Apresentação Comercial</title>
<link href="https://fonts.googleapis.com/css2?family=Montserrat:wght@500;700;800&family=Open+Sans:wght@400;600;700&display=swap" rel="stylesheet">
<style>
  :root{
    --navy:#1c2d4c;
    --navy-deep:#142340;
    --orange:#f26b1d;
    --orange-light:#f79a2e;
    --paper:#ffffff;
    --ink:#3a4660;
    --muted:#8a94a8;
    --ghost:rgba(255,255,255,.08);
    --ghost-dark:rgba(28,45,76,.08);
    --backdrop:#eceef1;
  }
  *{box-sizing:border-box;margin:0;padding:0}
  html,body{width:1200px;height:1200px;overflow:hidden;background:var(--backdrop)}
  body{font-family:"Open Sans",Arial,sans-serif;color:var(--ink);position:relative}
  .sheets{position:absolute;left:40px;top:316px;display:flex;gap:40px}
  .spread{display:flex;box-shadow:0 6px 24px rgba(0,0,0,.12)}
  .panel{width:270px;height:567px;position:relative;overflow:hidden;background:var(--paper)}
  .panel--cover{box-shadow:0 6px 24px rgba(0,0,0,.12)}
  .body-text{font-size:7.4px;line-height:1.55;margin-bottom:9px}

  /* intro panel */
  .panel--intro{padding:34px 24px 0}
  .panel--intro .body-text{color:var(--ink)}
  .intro-photo{position:absolute;left:0;right:0;top:318px;height:200px;
    background:linear-gradient(135deg,#dfe6ee 0%,#9fb2c8 45%,#2d3f5c 100%)}
  .intro-bar{position:absolute;left:0;right:0;bottom:0;height:49px;background:var(--orange)}

  /* specialties panel */
  .panel--specialties{background:var(--navy);padding:30px 22px 0;color:#d7dde8}
  .section-title{font-family:"Montserrat",Arial,sans-serif;font-weight:800;font-size:15px;letter-spacing:.5px;position:relative}
  .section-title .ghost{position:absolute;left:34px;top:9px;font-size:22px;white-space:nowrap;color:var(--ghost);z-index:0}
  .section-title .label{position:relative;z-index:1}
  .panel--specialties .section-title{color:#fff;margin-bottom:18px}
  .specialty{margin-bottom:14px}
  .specialty h3{font-family:"Montserrat",Arial,sans-serif;font-weight:700;font-size:8.5px;color:#fff;letter-spacing:.4px;margin-bottom:4px}
  .specialty .body-text{color:#c4ccd9;margin:0}
  .call-box{position:absolute;left:22px;right:22px;bottom:30px;background:var(--orange);padding:14px 14px;
    color:#fff;font-weight:600;font-size:8px;line-height:1.55}

  /* differentials panel */
  .panel--differentials{padding:0}
  .office-photo{height:150px;background:linear-gradient(160deg,#c9d3df 0%,#f3f4f6 40%,#b9c4d2 75%,#7f8fa6 100%)}
  .differentials-body{padding:16px 22px 0}
  .panel--differentials .section-title{color:var(--navy);margin-bottom:14px}
  .panel--differentials .section-title .ghost{color:var(--ghost-dark)}
  .differential{margin-bottom:10px}
  .differential h3{font-family:"Montserrat",Arial,sans-serif;font-weight:700;font-size:7.8px;color:var(--orange);letter-spacing:.3px;margin-bottom:3px}
  .differential .body-text{margin:0;color:var(--ink)}
  .diff-bar{position:absolute;left:0;right:0;bottom:0;height:16px;background:var(--navy)}

  /* cover */
  .cover-shape{position:absolute;left:0;top:0}
  .brand{position:absolute;left:26px;top:40px;display:flex;align-items:center;gap:8px;
    font-family:"Montserrat",Arial,sans-serif;font-weight:800;font-size:30px;color:var(--orange);letter-spacing:-.5px}
  .brand .dot{width:12px;height:12px;border-radius:50%;background:var(--navy)}
  .cover-photo{position:absolute;left:48px;top:168px;width:170px;height:170px;border-radius:50%;
    border:6px solid var(--paper);
    background:radial-gradient(circle at 40% 45%,#4a5d7a 0%,#22324f 55%,#0f1a2e 100%)}
  .cover-headline{position:absolute;left:26px;right:26px;top:378px;font-family:"Montserrat",Arial,sans-serif;
    font-weight:700;font-size:12.5px;line-height:1.4;color:#fff;text-transform:uppercase}
  .cover-foot{position:absolute;left:26px;right:26px;bottom:34px;font-size:8px;color:#fff;font-weight:600;
    border-top:1px solid rgba(255,255,255,.6);padding-top:7px}
</style>
</head>
<body>
<div class="sheets">
  <section class="spread" aria-label="Parte interna do folder">
    <article class="panel panel--intro">
      <p class="body-text">A Brumel Soluções é uma empresa especializada em soluções personalizadas de TI (Tecnologia da Informação).</p>
      <p class="body-text">Em resumo, ela “cuida” de tudo para que os seus funcionários não precisem se preocupar ou perder tempo com problemas técnicos de informática, como computador e/ou internet, falta de segurança dos arquivos, ausência de backups, softwares desatualizados e muito mais.</p>
      <p class="body-text">Com uma equipe proativa e altamente especializada, a Brumel Soluções consegue não apenas instalar os programas e equipamentos necessários como também realizar um monitoramento ativo para que a performance de todos os computadores da empresa se mantenha a mais elevada possível – 24 horas por dia, sete dias por semana.</p>
      <div class="intro-photo" role="img" aria-label="Foto de mãos de profissional de terno gesticulando diante de um notebook"></div>
      <div class="intro-bar"></div>
    </article>

    <article class="panel panel--specialties">
      <h2 class="section-title"><span class="ghost" aria-hidden="true">ESPECIALIDADES</span><span class="label">ESPECIALIDADES</span></h2>
      <p class="body-text">Atendemos empresas de diversos segmentos com soluções sob medida para cada rotina de trabalho.</p>
      <div class="specialty">
        <h3>COWORKING</h3>
        <p class="body-text">Espaços compartilhados exigem rede estável, acesso seguro e suporte rápido para cada novo membro que chega ao escritório.</p>
      </div>
      <div class="specialty">
        <h3>RESTAURANTE</h3>
        <p class="body-text">Sistemas de pedidos, caixa e estoque funcionando sem pausas, com suporte remoto durante todo o expediente.</p>
      </div>
      <div class="specialty">
        <h3>ADVOGADOS</h3>
        <p class="body-text">Proteção de documentos sigilosos, backups diários e acesso seguro aos processos de qualquer lugar.</p>
      </div>
      <div class="call-box">Deixe a tecnologia com a gente e concentre sua equipe no que realmente importa para o crescimento do seu negócio.</div>
    </article>

    <article class="panel panel--differentials">
      <div class="office-photo" role="img" aria-label="Foto de escritório moderno e claro com estações de trabalho"></div>
      <div class="differentials-body">
        <h2 class="section-title"><span class="ghost" aria-hidden="true">DIFERENCIAIS</span><span class="label">DIFERENCIAIS</span></h2>
        <div class="differential">
          <h3>ATENDIMENTO 24 HORAS</h3>
          <p class="body-text">Suporte disponível todos os dias da semana, inclusive feriados e finais de semana.</p>
        </div>
        <div class="differential">
          <h3>MONITORAMENTO ATIVO</h3>
          <p class="body-text">Acompanhamos seus equipamentos em tempo real e agimos antes que o problema apareça.</p>
        </div>
        <div class="differential">
          <h3>EQUIPE ESPECIALIZADA</h3>
          <p class="body-text">Técnicos certificados e atualizados com as principais tecnologias do mercado.</p>
        </div>
        <div class="differential">
          <h3>SEGURANÇA DOS DADOS</h3>
          <p class="body-text">Antivírus, firewall e políticas de acesso que mantêm seus arquivos protegidos.</p>
        </div>
        <div class="differential">
          <h3>BACKUP EM NUVEM</h3>
          <p class="body-text">Cópias automáticas e recuperação rápida de informações sempre que precisar.</p>
        </div>
      </div>
      <div class="diff-bar"></div>
    </article>
  </section>

  <article class="panel panel--cover" aria-label="Capa do folder">
    <svg class="cover-shape" width="270" height="567" viewBox="0 0 270 567" aria-hidden="true">
      <defs>
        <linearGradient id="coverOrange" x1="0" y1="0" x2="1" y2="1">
          <stop offset="0" stop-color="#f79a2e"/>
          <stop offset="1" stop-color="#f26b1d"/>
        </linearGradient>
      </defs>
      <polygon points="0,200 270,110 270,567 0,567" fill="url(#coverOrange)"/>
      <polygon points="0,200 270,110 270,128 0,218" fill="#f79a2e" opacity=".6"/>
    </svg>
    <div class="brand"><span class="dot"></span>Brumel</div>
    <div class="cover-photo" role="img" aria-label="Foto de mão tocando ícones digitais de tecnologia"></div>
    <h1 class="cover-headline">Alguma vez você já teve problemas com seu computador e não sabia a quem recorrer?</h1>
    <p class="cover-foot">Conheça nossas soluções em TI</p>
  </article>
</div>
</body>
</html>
```